Box insert for packaging of junior girls briefs

Need a insert to fit into our girls briefs packaging. Box is made of frosted plastic and measures 6 inches in width, 5 inches in height and 1.5 inches thick.

Box will have a open top flip as seen in photo of frosted envelope, same goes for closure.

Attached is a photo of a blank paper insert in a clear plastic box, that gives an idea as how I want it to look when inserted into the box. Note the small cutout of a brief to show what style this is. I would need to have same thing for hipster and bikini.
Design on packaging needs to be clean and sharp and appealing to junior girls and adults in their low 20's. Needs to be sophisticated but not provocative.
I'm uploading a EPS file of our logo. Basic logo layout should remain the same, however I'd like to see some creativity in making the logo more playful and young looking.
The front of the insert should have minimal information, maybe just size.
The back should contain information like website, contents, small size chart and country of origin (do in sample text).
Top of insert should have style number, size, logo and barcode. It can also have a picture (not cut out) of item style.

UPDATE: The front of the insert refers to the taller part and the back refers to the shorter part.

Plastic

• Must use our logo. It has been uploaded. Basic layout need to stay the same but you can change around the font and make it more playful. I might even consider a different color if it feels right.

```html
<!DOCTYPE html>
<html lang="en">
<head>
<meta charset="utf-8">
<title>Lumela Girls Briefs – Box Insert</title>
<link href="https://fonts.googleapis.com/css2?family=Poiret+One&family=Montserrat:wght@400;600;800&family=Comfortaa:wght@400&display=swap" rel="stylesheet">
<style>
  :root{
    --pink-light:#f8b6cc;
    --pink-mid:#f29abb;
    --pink-deep:#ec7fab;
    --magenta:#e6007e;
    --band:#e97aa5;
    --ink:#111111;
    --grey-row:#e4e5e6;
    --grey-line:#9a9a9a;
    --white:#ffffff;
    --skin:#f9d3c2;
    --garment-grey:#b9b9b9;
  }
  *{margin:0;padding:0;box-sizing:border-box}
  html,body{width:1200px;height:2200px;overflow:hidden}
  body{
    position:relative;
    font-family:"Montserrat",sans-serif;
    background:
      repeating-linear-gradient(125deg, rgba(255,255,255,.10) 0 38px, rgba(255,255,255,0) 38px 95px, rgba(236,110,160,.10) 95px 140px, rgba(255,255,255,0) 140px 210px),
      linear-gradient(125deg, var(--pink-light) 0%, var(--pink-mid) 45%, #f6b3c0 70%, var(--pink-deep) 100%);
  }
  .panel{position:absolute;left:0;width:1200px}
  .panel--back{top:0;height:800px}
  .panel--top{top:800px;height:403px;border-top:1px solid rgba(255,255,255,.35);border-bottom:1px solid rgba(255,255,255,.35)}
  .panel--front{top:1203px;height:865px}

  /* size chart (printed upside down for the back flap) */
  .chart-card{
    position:absolute;left:51px;top:73px;width:1101px;height:528px;
    background:var(--white);padding:22px 22px;
    transform:rotate(180deg);
  }
  .size-table{width:100%;border-collapse:collapse;font-size:13px;color:var(--ink)}
  .size-table td,.size-table th{border:1px solid var(--grey-line);text-align:center;height:53px;font-weight:400}
  .size-table th{height:30px;font-weight:600}
  .size-table .unit td{height:30px}
  .size-table .shade td{background:var(--grey-row)}
  .size-table .label{text-align:left;padding-left:10px;width:132px;font-weight:600;font-size:12px}
  .size-table .num{width:30px;border-left:none;border-top:none;border-bottom:none;font-weight:600}
  .size-table .gap td{height:10px;border-left:none;border-right:none}
  .chart-note{font-size:11px;border:1px solid var(--grey-line);padding:6px 10px;font-weight:600;letter-spacing:.3px}
  .chart-title{
    position:absolute;left:0;width:1200px;top:640px;text-align:center;
    font-family:"Poiret One",sans-serif;font-size:92px;color:var(--white);letter-spacing:6px;
    transform:rotate(180deg);
  }

  /* brand wordmark: name + tagline + one plain square */
  .brand{position:absolute}
  .brand__name{position:absolute;left:0;top:0;font-family:"Poiret One",sans-serif;font-weight:400;color:var(--ink);white-space:nowrap;line-height:1}
  .brand__tag{position:absolute;font-weight:800;color:var(--ink);white-space:nowrap;line-height:1}
  .brand__square{position:absolute;background:var(--magenta)}

  .brand--small{left:32px;top:150px;width:400px;height:140px}
  .brand--small .brand__name{font-size:100px}
  .brand--small .brand__tag{left:188px;top:108px;font-size:20px}
  .brand--small .brand__square{left:355px;top:106px;width:24px;height:24px}

  .brand--large{left:381px;top:185px;width:520px;height:190px}
  .brand--large .brand__name{font-size:131px}
  .brand--large .brand__tag{left:245px;top:145px;font-size:28px}
  .brand--large .brand__square{left:470px;top:142px;width:34px;height:34px}

  .barcode-area{position:absolute;left:804px;top:92px;width:326px;height:226px;background:var(--white)}

  .art{position:absolute;border-radius:14px}
  .art--bikini{background:linear-gradient(180deg,#f6c9b8,var(--skin))}
  .art--tankini{background:linear-gradient(180deg,#d9d9d9,var(--garment-grey))}
  .panel--top .art--bikini{left:396px;top:77px;width:154px;height:253px}
  .panel--top .art--tankini{left:587px;top:62px;width:183px;height:282px}
  .panel--front .art--bikini{left:147px;top:477px;width:198px;height:337px}
  .panel--front .art--tankini{left:804px;top:389px;width:260px;height:462px}

  .care{
    position:absolute;left:0;top:2068px;width:1200px;height:132px;background:var(--band);
    color:var(--white);font-family:"Comfortaa",sans-serif;font-size:22px;line-height:28px;
    padding:10px 70px 0;text-align:center;
  }
  .care strong{font-family:"Montserrat",sans-serif;font-weight:600}
</style>
</head>
<body>

<section class="panel panel--back">
  <div class="chart-card">
    <table class="size-table">
      <tr><th class="num"></th><th class="label"></th><th colspan="2">XS (5-6)</th><th colspan="2">S (7-8)</th><th colspan="2">M (10-12)</th><th colspan="2">L (14)</th><th colspan="2">XL (16)</th></tr>
      <tr class="unit"><td class="num"></td><td class="label"></td><td>IN</td><td>CM</td><td>IN</td><td>CM</td><td>IN</td><td>CM</td><td>IN</td><td>CM</td><td>IN</td><td>CM</td></tr>
      <tr class="shade"><td class="num">1.</td><td class="label">CHEST</td><td>25.5</td><td>65</td><td>27.5</td><td>70</td><td>29.5</td><td>75</td><td>32</td><td>81.5</td><td>34.5</td><td>88</td></tr>
      <tr><td class="num">2.</td><td class="label">SLEEVE LENGTH**</td><td>24.5</td><td>62.5</td><td>26.5</td><td>67.5</td><td>28.5</td><td>72.5</td><td>30.5</td><td>77.5</td><td>32.5</td><td>82.5</td></tr>
      <tr class="shade"><td class="num">3.</td><td class="label">WAIST</td><td>22.5</td><td>57</td><td>24.5</td><td>62</td><td>26.5</td><td>67.5</td><td>28.5</td><td>72.5</td><td>31</td><td>79</td></tr>
      <tr><td class="num">4.</td><td class="label">HIP</td><td>25.5</td><td>65</td><td>27.5</td><td>70</td><td>29.5</td><td>75</td><td>32</td><td>81.5</td><td>34.5</td><td>88</td></tr>
      <tr class="shade"><td class="num">5.</td><td class="label">INSEAM***</td><td>21</td><td>53.5</td><td>23</td><td>58.5</td><td>25.5</td><td>65</td><td>28.5</td><td>72</td><td>29.5</td><td>75</td></tr>
      <tr class="gap"><td colspan="12"></td></tr>
      <tr><td class="num">6.</td><td class="label">HEIGHT*</td><td>45</td><td>114</td><td>50</td><td>127</td><td>55</td><td>140</td><td>60</td><td>152.5</td><td>65</td><td>165</td></tr>
      <tr class="shade"><td class="num"></td><td class="label">WEIGHT*</td><td>42-49 LBS</td><td>19-22 KG</td><td>52-68 LBS</td><td>23.5-31 KG</td><td>71-87 LBS</td><td>32-39.5 KG</td><td>87-100 LBS</td><td>39.5-45 KG</td><td>102-112 LBS</td><td>46-51 KG</td></tr>
    </table>
    <p class="chart-note">*APPROXIMATE LENGTHS/WEIGHT &nbsp;**SLEEVE LENGTH FROM CENTER BACK NECK TO WRIST &nbsp;***INSEAM FROM ANKLE TO CROTCH</p>
  </div>
  <h2 class="chart-title">SIZE CHART</h2>
</section>

<section class="panel panel--top">
  <div class="brand brand--small">
    <span class="brand__name">LUMELA</span>
    <span class="brand__tag">GIRLS BRIEFS</span>
    <span class="brand__square"></span>
  </div>
  <div class="art art--bikini" role="img" aria-label="Illustration of a polka-dot bikini bra and brief"></div>
  <div class="art art--tankini" role="img" aria-label="Illustration of a grey halter tankini top"></div>
  <div class="barcode-area" role="img" aria-label="Space for product barcode"></div>
</section>

<section class="panel panel--front">
  <div class="brand brand--large">
    <span class="brand__name">LUMELA</span>
    <span class="brand__tag">GIRLS BRIEFS</span>
    <span class="brand__square"></span>
  </div>
  <div class="art art--bikini" role="img" aria-label="Illustration of a polka-dot bikini bra and brief"></div>
  <div class="art art--tankini" role="img" aria-label="Illustration of a grey halter tankini top"></div>
</section>

<footer class="care">
  <strong>Washing Instructions:</strong> Rinse twice, minimize spinning to reduce creasing. Do not use powder detergents or any products that contain fabric softeners, conditioners, stain removers or bleach as they will affect garment performance. Do not wash with heavily soiled clothing. Line dry your garment, or tumble dry it on a warm, gentle cycle.
</footer>

</body>
</html>
```